Card Design for my dog training business Rustpaw Obedience

Need a business card design for my dog training business with my new logo. Want the card to come off professional yet fun. Want it to be very eye catchy as well. I normally have these at vet clinics, pet stores, and groomers. so need it to look better than my competitors.
Target Market(s)
dog owners
Industry/Entity Type
Dog Training
Contact Information for Business Card
needs logo, my name and info
Font styles to use
Serif
Colors
0255a3
ffffff
ec1f27
000000
333333
fbfbfb
Requirements
Must have
- Rustpaw Obedience
- Hollis Brandt
- 415 903 2267
- info@rustpawobedience.example
- www.rustpawobedience.example

```html
<!DOCTYPE html>
<html lang="en">
<head>
<meta charset="utf-8">
<title>Rustpaw Obedience — Business Card</title>
<link rel="stylesheet" href="https://fonts.googleapis.com/css2?family=EB+Garamond:ital,wght@0,400;0,500;1,400&display=swap">
<style>
  :root {
    --page-bg: #2a2b2e;
    --card-bg: #1d1f21;
    --ink: #fbfbfb;
    --ink-soft: #c9c9c9;
    --rule: #e6e6e6;
  }
  * { box-sizing: border-box; margin: 0; padding: 0; }
  html, body { width: 1200px; height: 800px; overflow: hidden; }
  body {
    background: var(--page-bg);
    font-family: "EB Garamond", Georgia, serif;
    color: var(--ink);
    display: flex;
    align-items: center;
    justify-content: center;
    gap: 48px;
  }
  .card {
    width: 525px;
    height: 300px;
    background: var(--card-bg);
    border-radius: 3px;
    box-shadow: 0 14px 36px rgba(0,0,0,.45);
    position: relative;
    flex: none;
  }
  /* Front */
  .card--front {
    display: flex;
    flex-direction: column;
    align-items: center;
    justify-content: center;
  }
  .brand {
    display: flex;
    align-items: center;
    gap: 12px;
  }
  .brand__mark {
    width: 18px;
    height: 18px;
    border: 1.5px solid var(--ink);
    flex: none;
  }
  .brand__name {
    font-size: 34px;
    font-weight: 400;
    letter-spacing: 1px;
    color: var(--ink);
    white-space: nowrap;
  }
  .tagline {
    margin-top: 16px;
    font-style: italic;
    font-size: 13px;
    color: var(--ink-soft);
    letter-spacing: .3px;
    white-space: nowrap;
  }
  /* Back */
  .card--back {
    display: flex;
    align-items: center;
    padding: 0 0 0 58px;
  }
  .person {
    text-align: right;
    padding-right: 22px;
    white-space: nowrap;
  }
  .person__name {
    font-size: 24px;
    font-weight: 400;
    letter-spacing: .4px;
  }
  .person__role {
    font-size: 15px;
    color: var(--ink-soft);
  }
  .divider {
    width: 1.5px;
    height: 74px;
    background: var(--rule);
    flex: none;
  }
  .contact {
    list-style: none;
    padding-left: 20px;
    font-size: 14px;
    line-height: 1.55;
    white-space: nowrap;
  }
  .contact__item {
    display: flex;
    align-items: center;
    gap: 8px;
  }
  .contact__icon { width: 11px; height: 11px; flex: none; fill: var(--ink); }
</style>
</head>
<body>
  <section class="card card--front" aria-label="Card front">
    <div class="brand">
      <span class="brand__mark" aria-hidden="true"></span>
      <span class="brand__name">Rustpaw Obedience</span>
    </div>
    <p class="tagline">“Patient lessons for good dogs, one walk at a time.”</p>
  </section>

  <section class="card card--back" aria-label="Card back">
    <div class="person">
      <h1 class="person__name">Hollis Brandt</h1>
      <p class="person__role">Trainer</p>
    </div>
    <span class="divider" aria-hidden="true"></span>
    <ul class="contact">
      <li class="contact__item">
        <svg class="contact__icon" viewBox="0 0 24 24" aria-hidden="true"><path d="M6.6 10.8a15 15 0 0 0 6.6 6.6l2.2-2.2a1 1 0 0 1 1-.25 11.4 11.4 0 0 0 3.6.57 1 1 0 0 1 1 1V20a1 1 0 0 1-1 1A17 17 0 0 1 3 4a1 1 0 0 1 1-1h3.5a1 1 0 0 1 1 1c0 1.25.2 2.45.57 3.57a1 1 0 0 1-.25 1z"/></svg>
        415 903 2267
      </li>
      <li class="contact__item">
        <svg class="contact__icon" viewBox="0 0 24 24" aria-hidden="true"><path d="M2 5h20v14H2z M3.5 6.5 12 13l8.5-6.5" fill="none" stroke="#fbfbfb" stroke-width="2"/></svg>
        info@rustpawobedience.example
      </li>
      <li class="contact__item">
        <svg class="contact__icon" viewBox="0 0 24 24" aria-hidden="true"><circle cx="12" cy="12" r="10" fill="none" stroke="#fbfbfb" stroke-width="2"/><path d="M2 12h20M12 2c3 3 3 17 0 20M12 2c-3 3-3 17 0 20" fill="none" stroke="#fbfbfb" stroke-width="1.6"/></svg>
        www.rustpawobedience.example
      </li>
    </ul>
  </section>
</body>
</html>
```